Offshore Energy Projects Management Consultancy needs a business card design

Logo available. We provide teams to deliver engineering consultancy, project management and delivery teams mainly in the offshore renewables sector. The company is all about bringing the right people to a project to deliver the scope.

The business card will be used for all staff.

The business card should be quite simple, vibrant and uncluttered but convey experience, enthusiasm and integration.

Target Market(s)

Energy Project Developers and Tier 1 construction companies

Contact Information for Business Card

Logo should be on the back of the card. I'm happy for the designer to play with the colour of the logo and background colour.

Front of the card should convey all the must have information in a clear and professional manner but without being overly traditional.

Colors

Designer to choose colors to be used in the design.

Requirements
Must have
• Land Line Tel Number, Mobile Tel Number, Email, business address, web address.

```html
<!DOCTYPE html>
<html lang="en">
<head>
<meta charset="utf-8">
<title>Northwind Project Partners – Business Card</title>
<link href="https://fonts.googleapis.com/css2?family=Varela+Round&display=swap" rel="stylesheet">
<style>
  :root {
    --stage: #2b2b2d;
    --card-white: #f2f3f3;
    --brand-blue: #1d8fd6;
    --brand-blue-deep: #0f7fc4;
    --brand-blue-light: #2a9ad4;
    --logo-grey: #6b6e72;
    --ink: #1f1f22;
    --white: #ffffff;
  }
  * { box-sizing: border-box; margin: 0; padding: 0; }
  html, body { width: 1200px; height: 960px; overflow: hidden; }
  body {
    background: var(--stage);
    font-family: "Varela Round", sans-serif;
    position: relative;
  }
  .card {
    position: absolute;
    top: 165px;
    width: 360px;
    height: 630px;
    box-shadow: 0 14px 30px rgba(0,0,0,.45);
  }
  .card--front { left: 190px; background: var(--card-white); }
  .card--back {
    left: 650px;
    background: linear-gradient(180deg, var(--brand-blue-deep) 0%, var(--brand-blue-light) 100%);
  }

  .brand {
    position: absolute;
    left: 0; right: 0;
    text-align: center;
    font-size: 25px;
    line-height: 1.15;
    letter-spacing: .5px;
  }
  .card--front .brand { top: 90px; color: var(--logo-grey); }
  .card--back .brand { top: 250px; color: var(--white); }

  .person {
    position: absolute;
    top: 215px; left: 0; right: 0;
    text-align: center;
  }
  .person__name {
    color: var(--brand-blue);
    font-size: 30px;
    letter-spacing: 1.5px;
  }
  .person__role {
    color: var(--ink);
    font-size: 18px;
    margin-top: 4px;
  }

  .contact-icons {
    position: absolute;
    top: 330px; left: 0; right: 0;
    display: flex;
    justify-content: center;
    gap: 14px;
  }
  .contact-icons svg { width: 32px; height: 32px; display: block; }

  .contact-list {
    position: absolute;
    top: 385px; left: 0; right: 0;
    text-align: center;
    color: var(--ink);
    font-size: 19px;
    line-height: 1.45;
    list-style: none;
  }
  .contact-list .accent { color: var(--brand-blue); }

  .address {
    position: absolute;
    top: 498px; left: 0; right: 0;
    text-align: center;
    color: var(--ink);
    font-size: 18px;
    line-height: 1.4;
    font-style: normal;
  }
  .address svg { width: 26px; height: 30px; display: block; margin: 0 auto 6px; }

  .back-web {
    position: absolute;
    bottom: 60px; left: 0; right: 0;
    text-align: center;
    color: var(--white);
    font-size: 20px;
    letter-spacing: 2.5px;
  }
</style>
</head>
<body>

<section class="card card--front" aria-label="Business card front">
  <div class="brand">NORTHWIND<br>PROJECT PARTNERS</div>

  <div class="person">
    <h1 class="person__name">MARTIN HALE</h1>
    <p class="person__role">Founder &amp; CEO</p>
  </div>

  <div class="contact-icons">
    <svg viewBox="0 0 32 32" aria-label="Phone">
      <circle cx="16" cy="16" r="16" fill="var(--brand-blue)"/>
      <path d="M11.5 9.5l2.5-.5 1.5 3.5-1.7 1.2a9 9 0 0 0 4.5 4.5l1.2-1.7 3.5 1.5-.5 2.5c-.3 1-1.3 1.5-2.3 1.3A12 12 0 0 1 10.2 11.8c-.2-1 .3-2 1.3-2.3z" fill="none" stroke="#fff" stroke-width="1.4" stroke-linejoin="round"/>
    </svg>
    <svg viewBox="0 0 32 32" aria-label="Email">
      <circle cx="16" cy="16" r="16" fill="var(--brand-blue)"/>
      <rect x="8.5" y="11" width="15" height="10.5" rx="1" fill="#fff"/>
      <path d="M8.8 11.5l7.2 5.5 7.2-5.5" fill="none" stroke="var(--brand-blue)" stroke-width="1.3"/>
    </svg>
    <svg viewBox="0 0 32 32" aria-label="Website">
      <circle cx="16" cy="16" r="16" fill="var(--brand-blue)"/>
      <g fill="none" stroke="#fff" stroke-width="1.3">
        <circle cx="16" cy="16" r="7.5"/>
        <ellipse cx="16" cy="16" rx="3.3" ry="7.5"/>
        <path d="M8.5 16h15M9.6 12.2h12.8M9.6 19.8h12.8"/>
      </g>
    </svg>
  </div>

  <ul class="contact-list">
    <li>555.013.2290</li>
    <li>Martin@northwindpp.com</li>
    <li>www.<span class="accent">northwindpp</span>.com</li>
  </ul>

  <address class="address">
    <svg viewBox="0 0 26 30" aria-label="Location">
      <path d="M13 3a7 7 0 0 0-7 7c0 5 7 12 7 12s7-7 7-12a7 7 0 0 0-7-7z" fill="none" stroke="var(--brand-blue)" stroke-width="2"/>
      <circle cx="13" cy="10" r="2.5" fill="var(--brand-blue)"/>
      <path d="M5 24.5c2 2.5 14 2.5 16 0" fill="none" stroke="var(--brand-blue)" stroke-width="2" stroke-linecap="round"/>
    </svg>
    1180 Harbour Point Rd Ste. 310,<br>
    Portside, NC 28000-1100
  </address>
</section>

<section class="card card--back" aria-label="Business card back">
  <div class="brand">NORTHWIND<br>PROJECT PARTNERS</div>
  <p class="back-web">www.northwindpp.com</p>
</section>

</body>
</html>
```